Tarrow Consulting Needs Standardised Stationery!

Hello,I am looking at having some standardised stationery to continue building my brand. I am looking for a relatively clean and simple designs using the colours from my logos. Tarrow Consulting is the main business with Wayfield Careers Australia a subsidiary.
In particular I am after a design for:
- Letterhead (very important), white background, professional, corporate that I can send to prospective clients. Logo colours.
- Envelope, standard design I can print onto envelopes.
- Pens
- Other stationery/promotional items I can create

Target Market(s)

Universities, government, large organisations.

Industry/Entity Type

Professional Service

Font styles to use
Serif

Requirements
Must have
• Logo, match the design of the Tarrow Consulting logo. Black Wayfield Careers Australia logo is a subsidiary.
Should not have
• Too much colour, some colour is good, but I am looking for a clean professional look.

```html
<!DOCTYPE html>
<html lang="en">
<head>
<meta charset="utf-8">
<title>Tarrow Consulting Letterhead</title>
<link href="https://fonts.googleapis.com/css2?family=Open+Sans:wght@400;600&family=Lato:wght@400;700&family=Montserrat:wght@500&display=swap" rel="stylesheet">
<style>
  :root {
    --backdrop: #d9d9d9;
    --paper: #ffffff;
    --ink: #3d3d3d;
    --ink-soft: #4a4a4a;
    --brand-dark: #1f1f1f;
    --band-blue: #0f93cf;
    --band-green: #00a651;
    --band-orange: #e38431;
  }
  * { margin: 0; padding: 0; box-sizing: border-box; }
  html, body { width: 1040px; height: 1200px; overflow: hidden; background: var(--backdrop); }
  .letterhead {
    position: absolute; left: 54px; top: 0; width: 932px; height: 1200px;
    background: var(--paper); font-family: "Open Sans", sans-serif; color: var(--ink-soft);
  }
  .brand { position: absolute; left: 290px; top: 38px; display: flex; align-items: center; gap: 22px; }
  .brand-square { width: 44px; height: 44px; background: var(--brand-dark); }
  .brand-name {
    font-family: "Montserrat", sans-serif; font-weight: 500; color: var(--brand-dark);
    font-size: 40px; letter-spacing: 1px; line-height: 1;
  }
  .brand-name span { display: block; font-size: 17px; letter-spacing: 13px; margin-top: 4px; }
  .text { position: absolute; left: 87px; width: 754px; font-size: 15px; line-height: 18px; }
  .issue-date { top: 217px; }
  .recipient { top: 253px; }
  .salutation { top: 357px; }
  .body-para { line-height: 27px; text-align: justify; hyphens: auto; -webkit-hyphens: auto; }
  .p1 { top: 410px; } .p2 { top: 572px; } .p3 { top: 680px; }
  .closing { top: 815px; }
  .signer-name { top: 892px; font-size: 19px; font-weight: 600; color: var(--ink); line-height: 24px; }
  .signer-title { top: 923px; }
  .subsidiary {
    position: absolute; left: 0; width: 932px; top: 1040px; display: flex; justify-content: center;
    align-items: center; gap: 6px; font-family: "Lato", sans-serif; font-weight: 700; font-size: 13px; color: var(--brand-dark);
  }
  .subsidiary-dot { width: 22px; height: 22px; border-radius: 50%; background: var(--brand-dark); }
  .contact-bands { position: absolute; top: 1083px; left: 0; width: 932px; height: 61px; }
  .band {
    position: absolute; top: 0; height: 61px; display: flex; align-items: center; justify-content: center;
    font-family: "Lato", sans-serif; font-size: 17px; color: #fff;
  }
  .band b { font-weight: 700; margin-right: 4px; }
  .band-phone { left: 0; width: 302px; background: var(--band-blue); }
  .band-email { left: 306px; width: 311px; background: var(--band-green); }
  .band-web { left: 620px; width: 312px; background: var(--band-orange); }
  .postal { position: absolute; top: 1161px; left: 0; width: 932px; text-align: center; font-family: "Lato", sans-serif; font-size: 14px; color: var(--brand-dark); }
</style>
</head>
<body>
<main class="letterhead">
  <div class="brand">
    <div class="brand-square"></div>
    <div class="brand-name">TARROW<span>CONSULTING</span></div>
  </div>

  <p class="text issue-date">Issuing Date: May 5, 2018</p>
  <p class="text recipient">Name Of Employee Mr. XYZABC<br>Address of Employee<br>Address Line 2 etc..</p>
  <p class="text salutation">Dear Mr.XYZABC</p>

  <p class="text body-para p1">Lorem Ipsum has been the industry's standard dummy text ever since the 1500s, when an unknown printer took a galley of type and scrambled it to make a type specimen book. It has survived not only five centuries, but also the leap into electronic typesetting, remaining essentially unchanged. It was popularised in the 1960s with the release of dry-transfer sheets containing Lorem Ipsum passages, and more recently with desktop publishing software like early page layout programs including versions of Lorem Ipsum.</p>
  <p class="text body-para p2">Lorem Ipsum is simply dummy text of the printing and typesetting industry. Lorem Ipsum has been the industry's standard dummy text ever since the 1500s, when an unknown printer took a galley of type and scrambled it to make a type specimen book.</p>
  <p class="text body-para p3">It has survived not only five centuries, but also the leap into electronic typesetting, remaining essentially unchanged. It was popularised in the 1960s with the release of dry-transfer sheets containing Lorem IpsumIpsum passages.</p>

  <p class="text closing">Yours Sincerely</p>
  <p class="text signer-name">Daniel Hartley</p>
  <p class="text signer-title">Managing Director</p>

  <div class="subsidiary"><div class="subsidiary-dot"></div>Wayfield Careers Australia</div>

  <div class="contact-bands">
    <div class="band band-phone"><b>P:</b>044-555 018 274</div>
    <div class="band band-email"><b>E:</b>info@tarrowconsult.com</div>
    <div class="band band-web">www.tarrowconsult.com</div>
  </div>
  <p class="postal">421, Address line here,&nbsp; dummy code 45452 Country Name</p>
</main>
</body>
</html>
```